Flyer-Design mit Bio-Charakter für  Direktverkauf von FeldKrone
Flyer-Design mit Bio-Charakter für Direktverkauf von FeldKrone
Zielgruppe
Es geht um Direktverkauf von FeldKrone (Bio), Informationen über www.hofzumfirst.ch
Wir möchten einen Flyer bei welchem die Preise ersichtlich sind (Einzelpreis / Paketpreis) alles auf der Homepage ersichtlich.
Aufgabenstellung
Da sind wir offen für alles, Wichtig ist der Bio-Charakter, die Liebe zu den Tieren. Der Flyer sollte A5 oder ein Faltprospekt sein.
Eventuell wird dieser noch durch Vermarktung mit Holz und später noch einen Bio-Hofladen erweitert, aber erst im nächsten Jahr, daher relevant ist im Moment ein Flyer für das Fleisch.
Wenn möglich sollte das Datenformat am Schluss AdobeInDesign sein.
Falls wir eigene Fotos senden sollen, einfach melden (Fotos der Bauerfamilie, Hof, etc.)

```html
<!DOCTYPE html>
<html lang="de">
<head>
<meta charset="utf-8">
<title>Preisliste FeldKrone – Hof zum First</title>
<link href="https://fonts.googleapis.com/css2?family=Open+Sans:wght@400;700&family=Roboto+Condensed:wght@700&display=swap" rel="stylesheet">
<style>
  :root {
    --paper: #fdfcf8;
    --paper-gap: #f6f4ee;
    --ink: #3b2a25;
    --green: #74ae55;
    --rule: #cfc8c0;
  }
  * { margin: 0; padding: 0; box-sizing: border-box; }
  html, body { width: 846px; height: 1200px; overflow: hidden; background: var(--paper); }
  body { position: relative; font-family: "Open Sans", sans-serif; color: var(--ink); }

  .fold { position: absolute; left: 416px; top: 0; width: 12px; height: 1200px; background: var(--paper-gap); }

  .badge { position: absolute; left: 62px; top: 34px; width: 44px; height: 44px; border-radius: 50%; background: var(--green); }

  .brand { position: absolute; right: 30px; top: 70px; display: flex; align-items: center; gap: 12px; }
  .brand-dot { width: 34px; height: 34px; border-radius: 50%; background: #d9b48c; }
  .brand-name { font-weight: 700; font-size: 30px; color: var(--green); line-height: 1; }
  .brand-sub { position: absolute; right: 30px; top: 108px; font-weight: 700; font-size: 11px; letter-spacing: 1px; color: var(--ink); }

  .eyebrow { font-family: "Roboto Condensed", sans-serif; font-weight: 700; font-size: 23px; line-height: 1; text-transform: uppercase; }
  .title { font-family: "Roboto Condensed", sans-serif; font-weight: 700; font-size: 40px; line-height: 1; color: var(--green); text-transform: uppercase; }

  .left-head { position: absolute; left: 29px; top: 145px; }
  .left-head .title { margin-top: 8px; }

  .price-list { position: absolute; left: 29px; top: 229px; width: 365px; list-style: none; }
  .price-list li { height: 45px; display: flex; justify-content: space-between; align-items: center; border-bottom: 1px dashed var(--rule); font-size: 20.5px; }
  .price-list .price { font-weight: 700; }

  .separate-head { position: absolute; left: 29px; top: 938px; font-size: 22px; }
  .separate-list { position: absolute; left: 29px; top: 970px; width: 365px; list-style: none; font-size: 20.5px; }
  .separate-list li { display: flex; justify-content: space-between; align-items: flex-start; border-bottom: 1px dashed var(--rule); line-height: 26px; padding: 3px 0 10px; }
  .separate-list li.single { padding: 5px 0 8px; }
  .separate-list .price { font-weight: 700; }
  .note-liver { position: absolute; left: 29px; top: 1134px; font-size: 20.5px; }

  .right-head { position: absolute; right: 30px; top: 218px; text-align: right; }
  .right-head .title { margin-top: 8px; }

  .packages { position: absolute; left: 451px; top: 302px; width: 365px; list-style: none; font-size: 20.5px; }
  .packages li { display: flex; justify-content: space-between; align-items: flex-start; border-bottom: 1px dashed var(--rule); line-height: 27px; padding: 8px 2px 10px 0; }

  .contents { position: absolute; right: 30px; top: 512px; width: 370px; text-align: right; font-size: 20.5px; line-height: 30.5px; }
  .contents strong { font-weight: 700; }
  .package-price { position: absolute; right: 30px; top: 716px; font-weight: 700; font-size: 36px; color: var(--green); }

  .notes { position: absolute; right: 30px; top: 826px; width: 370px; text-align: right; font-size: 16px; line-height: 26px; }
  .notes p { margin-bottom: 25px; }
  .notes .highlight { color: var(--green); font-weight: 700; margin-bottom: 0; }
</style>
</head>
<body>
  <div class="fold"></div>

  <div class="badge" role="img" aria-label="Zertifikatssiegel Umstellung"></div>

  <div class="brand"><span class="brand-dot"></span><span class="brand-name">Hof zum First</span></div>
  <div class="brand-sub">HOFLADEN FAMILIE KESSLER</div>

  <header class="left-head">
    <div class="eyebrow">Preisliste</div>
    <div class="title">FeldKrone pro kg</div>
  </header>

  <ul class="price-list">
    <li><span>Geschnetzeltes</span><span class="price">41,00 CHF/kg</span></li>
    <li><span>Plätzli a la Minute</span><span class="price">50,50 CHF/kg</span></li>
    <li><span>Hackfleisch</span><span class="price">23,50 CHF/kg</span></li>
    <li><span>Hamburger</span><span class="price">29,00 CHF/kg</span></li>
    <li><span>Braten</span><span class="price">29,50 CHF/kg</span></li>
    <li><span>Saftplätzli</span><span class="price">40,00 CHF/kg</span></li>
    <li><span>Voressen</span><span class="price">26,50 CHF/kg</span></li>
    <li><span>Siedfleich</span><span class="price">25,00 CHF/kg</span></li>
    <li><span>Hohrrückensteak</span><span class="price">58,00 CHF/kg</span></li>
    <li><span>Huftsteak</span><span class="price">74,00 CHF/kg</span></li>
    <li><span>Entrecote</span><span class="price">77,00 CHF/kg</span></li>
    <li><span>Filet</span><span class="price">89,00 CHF/kg</span></li>
    <li><span>Bäggli</span><span class="price">42,00 CHF/kg</span></li>
    <li><span>Zunge</span><span class="price">25,00 CHF/kg</span></li>
    <li><span>Leberli</span><span class="price">22,50 CHF/kg</span></li>
  </ul>

  <div class="eyebrow separate-head">Separat beziehen:</div>
  <ul class="separate-list">
    <li><span>Rindszunge<br>gesalzen &amp; geräuchert</span><span class="price">1x pro Tier</span></li>
    <li class="single"><span>Ochsenschwanz</span><span class="price">1x pro Tier</span></li>
    <li class="single"><span>Ochsenbäggli</span><span class="price">xx,xx CHF/kg</span></li>
  </ul>
  <div class="note-liver">Leber in 300g Portionen</div>

  <header class="right-head">
    <div class="eyebrow">Preisliste</div>
    <div class="title">Mischpakete</div>
  </header>

  <ul class="packages">
    <li><span>Mischpaket 10kg</span><span>ohne Filet</span></li>
    <li><span>Mischpaket 1/8<br>20-25kg</span><span>mit Filet</span></li>
    <li><span>Mischpaket 1/4<br>40-50kg</span><span>mit Filet</span></li>
  </ul>

  <div class="contents">
    <strong>Die Pakete enthalten</strong><br>
    Geschnetzeltes, Plätzli ala Minute, Entrecote, Siedfleisch, Hackfleisch, Braten, Hamburger, Filet (ab 1/8), Saftplätzli, Voressen, Huft und/oder Hohrückensteak.
  </div>
  <div class="package-price">32,50 CHF/kg</div>

  <div class="notes">
    <p>Das Fleisch wird von uns portioniert,<br>vakummiert und beschriftet.</p>
    <p>Auf persönliche Wünsche wie <strong>„ohne Siedfleisch und/oder ohne Hamburger“</strong> kann eingegangen werden, dies wird mit mehr Hackfleisch ergänzt.</p>
    <p class="highlight">Haben Sie Interesse an kleineren Mengen oder Einzelstücken?</p>
    <p>Zu den Abholterminen einfach vorbeikommen, ganz nach dem Motto:<br><strong>„äs hät so langs hät“</strong></p>
  </div>
</body>
</html>
```